Gently Windswept needs an eye catching marketing flyer

Our new Lumenvale Method(r) business needs an eye catching marketing flyer. We think A5 sizing?
website link (where you can understand more about breathwork is www.gentlywindswept-example.co.uk)
Design whatever you would like to design some things that could be of use to mention are below. Will leave it in your capable hands.
Logo files for Gently Windswept attached, use whichever one is best for your design, should be the main logo and colour scheme for the flyer, the second logo is that of Lumenvale Method(r) the breath school who's body of work we will be delivering. This can be anywhere on the flyer
Flyer is needed to get people interested in breathwork, the potential benefits for breathing better
We offer 1:1 sessions, workshops, corporate training
The flyer will have an offer code 'OpenDoor' which will give 15% off the bookers first 1:1 session
Flyer should include the following contact details: Maybe a "find out how breathwork can help you today. . . "
Carol Pennick (South): 07700 900 318
Rosalind Tarrow (Midlands): 07700 900 742
facebook: we.are.gentlywindswept
instagram: _gentlywindswept_

```html
<!DOCTYPE html>
<html lang="en">
<head>
<meta charset="utf-8">
<title>Gently Windswept – Breathwork Flyer</title>
<link rel="stylesheet" href="https://fonts.googleapis.com/css2?family=Noto+Serif:wght@400;700&family=Montserrat:wght@400&display=swap">
<style>
  :root {
    --cream: #f0dccf;
    --royal: #0a3bb8;
    --navy: #06207a;
    --deep: #0b1a63;
    --ink: #111111;
    --slate: #555555;
    --link-blue: #2a2ad6;
    --code-red: #e3120f;
    --tan: #c98463;
    --crimson: #931a1a;
    --ring: #f4f4f4;
    --outline: #1a4cf0;
    --white: #ffffff;
    --plum: #5a2d91;
  }
  * { margin: 0; padding: 0; box-sizing: border-box; }
  html, body { width: 849px; height: 1200px; overflow: hidden; background: #ffffff; }
  .flyer {
    position: relative; width: 849px; height: 1200px; overflow: hidden;
    background: var(--cream);
    font-family: "Noto Serif", Georgia, serif; font-weight: 700;
  }
  .backdrop { position: absolute; inset: 0; }
  .text { position: absolute; text-align: center; text-transform: uppercase; white-space: nowrap; }
  .brand-name {
    left: 560px; top: 88px; width: 170px; color: var(--white);
    font-size: 22px; line-height: 1.15; text-transform: none; font-weight: 400; white-space: normal;
  }
  .invite { left: 0; top: 692px; width: 388px; color: var(--slate); font-size: 17px; letter-spacing: 4px; line-height: 26px; }
  .contacts { left: 0; top: 810px; width: 398px; font-size: 15px; letter-spacing: 2.8px; line-height: 21.3px; color: var(--ink); }
  .contacts .detail { color: var(--link-blue); }
  .partner-name { left: 315px; top: 1050px; width: 100px; color: var(--plum); font-family: "Montserrat", Arial, sans-serif; font-weight: 400; font-size: 9px; line-height: 11px; text-transform: none; }
  .web { left: 0; top: 1103px; width: 425px; color: var(--white); font-size: 13.5px; letter-spacing: 3px; line-height: 23px; }
  .web .label { font-size: 17px; letter-spacing: 3px; font-variant: small-caps; text-transform: none; }
  .offer { left: 500px; top: 700px; width: 326px; color: var(--white); font-size: 16px; letter-spacing: 3.6px; line-height: 25px; }
  .code-label { left: 500px; top: 876px; width: 300px; color: var(--white); font-size: 17px; letter-spacing: 4px; }
  .code { left: 480px; top: 912px; width: 340px; color: var(--code-red); font-size: 32px; letter-spacing: 4px; line-height: 44px; }
  .discount { left: 480px; top: 978px; width: 340px; color: var(--white); font-size: 17px; letter-spacing: 4px; line-height: 25px; }
</style>
</head>
<body>
<main class="flyer">
  <svg class="backdrop" width="849" height="1200" viewBox="0 0 849 1200">
    <defs>
      <linearGradient id="panelBlue" x1="0" y1="0" x2="0" y2="1">
        <stop offset="0" stop-color="#0a3fd0"/>
        <stop offset="0.55" stop-color="#0a2a9a"/>
        <stop offset="1" stop-color="#0b1f70"/>
      </linearGradient>
      <linearGradient id="photoTones" x1="0" y1="0" x2="1" y2="1">
        <stop offset="0" stop-color="#b78a6c"/>
        <stop offset="0.5" stop-color="#8a5b45"/>
        <stop offset="1" stop-color="#3b2a2a"/>
      </linearGradient>
      <clipPath id="photoClip"><circle cx="310" cy="262" r="400"/></clipPath>
    </defs>

    <rect class="panel-blue" x="425" y="0" width="424" height="1116" fill="url(#panelBlue)"/>
    <polygon class="panel-facet" points="425,724 849,915 849,1116 425,1116" fill="#102c8a"/>
    <polygon class="panel-shadow" points="425,724 849,915 849,760 425,690" fill="#081a66" opacity="0.6"/>
    <rect class="footer-dark" x="425" y="1116" width="424" height="84" fill="#000000"/>
    <path class="footer-wave-edge" d="M0,1044 C180,1030 380,1070 470,1110 C520,1135 520,1170 520,1200 L0,1200 Z" fill="#000000"/>
    <path class="footer-wave" d="M0,1052 C180,1040 370,1080 460,1118 C510,1140 515,1170 520,1200 L0,1200 Z" fill="var(--royal)"/>

    <polygon class="corner-shade" points="425,650 425,724 393,714 410,660" fill="#3a1418"/>

    <circle class="photo-outline" cx="310" cy="262" r="412" fill="var(--outline)"/>
    <circle class="photo-ring" cx="310" cy="262" r="410" fill="var(--ring)"/>
    <circle class="photo" cx="310" cy="262" r="400" fill="url(#photoTones)" role="img" aria-label="Photo of a breathwork session: a practitioner supporting a client lying on blankets on the floor, others resting nearby"/>
    <polygon class="crimson-veil" clip-path="url(#photoClip)" points="643,0 849,0 849,714 393,714" fill="var(--crimson)" opacity="0.42"/>

    <path class="brand-arc-outline" d="M369,0 C400,140 560,232 720,232 C790,232 830,218 849,205 L849,0 Z" fill="var(--outline)"/>
    <path class="brand-arc" d="M369,0 C400,130 555,222 715,222 C785,222 830,208 849,195 L849,0 Z" fill="var(--tan)"/>
    <path class="brand-arc-red" d="M643,0 L849,0 L849,195 C830,208 785,222 715,222 C660,222 620,212 576,198 Z" fill="var(--crimson)"/>
    <circle class="brand-mark" cx="632" cy="110" r="68" fill="none" stroke="#1f4fe0" stroke-width="1.5"/>

    <line class="divider" x1="0" y1="766" x2="200" y2="766" stroke="#1a3cc8" stroke-width="4"/>
    <circle class="divider-dot" cx="207" cy="766" r="13" fill="#1a3cc8"/>

    <g class="arrow" fill="none" stroke="#ffffff" stroke-width="2.5" stroke-linecap="round" stroke-linejoin="round">
      <path d="M428,716 C433,711 437,720 443,714 L452,714"/>
      <path d="M447,709 L453,714 L447,719"/>
      <path d="M428,890 C433,885 437,894 443,888 L452,888"/>
      <path d="M447,883 L453,888 L447,893"/>
    </g>

    <circle class="partner-badge" cx="365" cy="1008" r="37" fill="#5a2d91"/>

    <g class="social-row" fill="none" stroke="#ffffff" stroke-width="1.5">
      <line x1="168" y1="1160" x2="168" y2="1176"/><line x1="172" y1="1160" x2="172" y2="1176"/>
      <circle cx="186" cy="1168" r="6"/>
      <line x1="200" y1="1160" x2="200" y2="1176"/><line x1="204" y1="1160" x2="204" y2="1176"/>
      <circle cx="217" cy="1168" r="6"/>
      <line x1="230" y1="1160" x2="230" y2="1176"/><line x1="234" y1="1160" x2="234" y2="1176"/>
      <circle cx="247" cy="1168" r="6"/>
      <line x1="260" y1="1160" x2="260" y2="1176"/><line x1="264" y1="1160" x2="264" y2="1176"/>
    </g>
  </svg>

  <div class="text brand-name">Gently Windswept</div>

  <p class="text invite">Find out how breathwork<br>can help you today. .</p>

  <div class="text contacts">
    <div>Carol Pennick (South):</div>
    <div class="detail">07700 900 318</div>
    <div>Rosalind Tarrow (Midlands):</div>
    <div class="detail">07700 900 742</div>
    <div>Facebook:</div>
    <div class="detail">we.are.gentlywindswept</div>
    <div>Instagram:</div>
    <div class="detail">_gentlywindswept_</div>
  </div>

  <div class="text partner-name">Lumenvale<br>Method®</div>

  <div class="text web">
    <div class="label">WebSite:</div>
    <div>www.gentlywindswept-example.co.uk</div>
  </div>

  <p class="text offer">We offer 1:1 sessions,<br>workshops, corporate<br>training!</p>
  <p class="text code-label">Use code</p>
  <p class="text code">OpenDoor</p>
  <p class="text discount">And get 15% off on the<br>first 1:1 session</p>
</main>
</body>
</html>
```